professional health club Info Flyer

we need a professional health club DL flyer that will provide information regarding our 24/7 health club services to enquiries whilst we are unstaffed. these will be placed outside on main street.

www.fitrova.club

On the reverse side, we want to offer 2 introductory specials;
1. free 7 day trial
2. Membership, classes & personal training introductory month3 personal training sessions and month 24/7 membership and classes for $99.95 (saving of over $159.85)
conditions: valid for new members only

SIZE: DL with double sided

Target Market(s)

professional, male and female of all ages (in particular those 30+)

Industry/Entity Type

Health And Wellness

Colors
33a6d7
abd037
f78f20
ffffff

Requirements
Must have
• - professional allied health feel about flyer with images
• - contact details
• - services provided include 24/7 memberships, classes, special population group training, Exercise physiology, physiotherapy, massage, nutrition, rehabilitation.
• - a catch to get them to contact us
• - our slogan "We are here to improve your quality of life"

```html
<!DOCTYPE html>
<html lang="en">
<head>
<meta charset="utf-8">
<title>Fitrova Health Club – DL Flyer</title>
<link href="https://fonts.googleapis.com/css2?family=Oswald:wght@400;500;600&family=Arimo:ital,wght@0,400;0,700;1,700&display=swap" rel="stylesheet">
<style>
:root{
  --stage:#7b1d12;
  --orange:#f7921e;
  --green:#55c91e;
  --blue:#33a6d7;
  --navy:#1d2f8a;
  --ink:#222222;
  --dark:#111111;
  --paper:#f4f4f4;
  --tick:#d81f2a;
  --white:#ffffff;
}
*{margin:0;padding:0;box-sizing:border-box}
html,body{width:1200px;height:1000px;overflow:hidden}
body{background:var(--stage);position:relative;font-family:"Arimo",Arial,sans-serif;color:var(--ink)}
.flyer{position:absolute;width:973px;height:459px;background:var(--paper);overflow:hidden}
.flyer--front{left:115px;top:38px}
.flyer--back{left:113px;top:515px;height:458px}
.flyer svg.art{position:absolute;left:0;top:0}
.brand{position:absolute;display:flex;align-items:center;gap:8px}
.brand__dot{width:34px;height:34px;border-radius:50%;background:var(--blue)}
.brand__name{font-family:"Oswald",sans-serif;font-weight:500;font-size:30px;color:var(--blue);line-height:1;letter-spacing:.5px}
.slogan{position:absolute;font-family:"Arimo",sans-serif;font-style:italic;font-weight:700;color:var(--navy);white-space:nowrap}
.join{position:absolute;left:30px;top:22px;width:245px;height:58px;display:flex;align-items:center;justify-content:center;
  font-family:"Oswald",sans-serif;font-weight:600;font-size:46px;color:#2b2b2b;letter-spacing:-.5px}
.mission{position:absolute;left:289px;top:88px;width:324px;font-size:12px;line-height:13px;color:var(--ink)}
.mission p+p{margin-top:13px}
.expertise__title{position:absolute;left:348px;top:190px;font-family:"Oswald",sans-serif;font-weight:500;font-size:27px;color:#2b2b2b}
.expertise__list{position:absolute;left:360px;top:228px;list-style:none;width:300px}
.expertise__list li{display:flex;align-items:flex-start;gap:5px;font-family:"Oswald",sans-serif;font-weight:500;font-size:13px;line-height:19px;color:var(--navy);text-transform:uppercase}
.expertise__list li svg{flex:none;margin-top:2px}
.services__title{position:absolute;left:0;width:973px;text-align:center;top:30px;font-family:"Oswald",sans-serif;font-weight:500;font-size:34px;color:#2b2b2b;letter-spacing:.3px}
.service-label{position:absolute;transform:translateX(-50%);white-space:nowrap;font-family:"Oswald",sans-serif;font-size:14px;color:var(--dark)}
.offer__tag{position:absolute;left:15px;top:343px;height:32px;padding:0 18px 0 14px;display:flex;align-items:center;font-family:"Oswald",sans-serif;font-weight:500;font-size:18px;color:#1a1a1a}
.offer__headline{position:absolute;left:227px;top:336px;font-family:"Oswald",sans-serif;font-weight:500;font-size:34px;color:#1a1a1a}
.offer__terms{position:absolute;left:37px;top:385px;width:450px;font-size:11px;line-height:14px;color:var(--dark)}
.contact__tab{position:absolute;left:532px;top:363px;width:128px;height:28px;display:flex;align-items:center;justify-content:center;font-family:"Oswald",sans-serif;font-weight:500;font-size:15px;color:var(--dark)}
.contact__phone{position:absolute;left:633px;top:395px;font-family:"Oswald",sans-serif;font-weight:500;font-size:24px;color:var(--white)}
.contact__address{position:absolute;left:800px;top:397px;font-size:10.5px;line-height:13px;color:var(--white);font-weight:700;border-left:2px solid var(--white);padding-left:6px}
.contact__web{position:absolute;left:638px;top:432px;font-size:11px;font-weight:700;color:var(--white)}
</style>
</head>
<body>

<section class="flyer flyer--front">
  <svg class="art" width="973" height="459" viewBox="0 0 973 459">
    <defs>
      <linearGradient id="gymFront" x1="0" y1="0" x2="1" y2="1">
        <stop offset="0" stop-color="#f2f2f2"/><stop offset=".55" stop-color="#dcdcdc"/><stop offset="1" stop-color="#c4c4c4"/>
      </linearGradient>
      <linearGradient id="personTone" x1="0" y1="0" x2="1" y2="1">
        <stop offset="0" stop-color="#f3d9bd"/><stop offset=".3" stop-color="#e4b58e"/><stop offset=".5" stop-color="#2aa3dc"/><stop offset=".75" stop-color="#1f2840"/><stop offset="1" stop-color="#e85a4f"/>
      </linearGradient>
      <linearGradient id="hexTrainer" x1="0" y1="0" x2="1" y2="1">
        <stop offset="0" stop-color="#f1f1f1"/><stop offset=".4" stop-color="#d6a98a"/><stop offset=".7" stop-color="#3a3a3a"/><stop offset="1" stop-color="#b9b9b9"/>
      </linearGradient>
      <linearGradient id="hexMachine" x1="0" y1="0" x2="1" y2="1">
        <stop offset="0" stop-color="#e9e9e9"/><stop offset=".5" stop-color="#5a5a5a"/><stop offset="1" stop-color="#2b2b2b"/>
      </linearGradient>
      <linearGradient id="hexGym" x1="0" y1="0" x2="1" y2="1">
        <stop offset="0" stop-color="#eef6fa"/><stop offset=".45" stop-color="#4fb4df"/><stop offset="1" stop-color="#3b4048"/>
      </linearGradient>
      <filter id="shadowF" x="-10%" y="-10%" width="120%" height="120%"><feDropShadow dx="2" dy="3" stdDeviation="3" flood-opacity=".45"/></filter>
    </defs>
    <rect width="973" height="459" fill="url(#gymFront)" role="img" aria-label="Faded photo of a gym floor with training machines"/>
    <polygon points="0,0 545,0 525,24 0,24" fill="var(--orange)"/>
    <polygon points="525,24 545,0 560,0 535,30 0,30 0,24" fill="#3a3a3a"/>
    <polygon points="0,175 0,459 370,459" fill="#2a2a2a"/>
    <path d="M0 140 H250 Q330 200 335 300 L335 459 H0 Z" fill="url(#personTone)" opacity=".9" role="img" aria-label="Photo of a smiling woman in sportswear stretching on the floor"/>
    <polygon points="915,12 973,12 973,200 830,200" fill="var(--green)"/>
    <polygon points="800,300 973,300 973,459 900,459" fill="var(--blue)"/>
    <polygon points="790,350 890,350 920,459 800,459" fill="var(--orange)"/>
    <polygon points="32,24 278,18 276,78 110,80 86,104 88,80 30,82" fill="#ffffff" stroke="#2a2a2a" stroke-width="3"/>
    <g filter="url(#shadowF)">
      <polygon points="631,187 671,118 751,118 791,187 751,256 671,256" fill="url(#hexTrainer)" stroke="#2a2a2a" stroke-width="6" role="img" aria-label="Photo of a trainer guiding a woman through a shoulder exercise"/>
      <polygon points="792,257 836,181 924,181 968,257 924,333 836,333" fill="url(#hexMachine)" stroke="#2a2a2a" stroke-width="6" role="img" aria-label="Photo of cable machine handles in the gym"/>
      <polygon points="645,361 686,290 768,290 809,361 768,432 686,432" fill="url(#hexGym)" stroke="#2a2a2a" stroke-width="6" role="img" aria-label="Photo of the gym interior with training machines"/>
    </g>
  </svg>

  <div class="join">JOIN NOW!</div>

  <div class="mission">
    <p>This is our mission. We understand everyone has different requirements to improve their quality of life. This is the sole reason Fitrova Health Club has developed into a friendly yet professional environment with flexible options.</p>
    <p>We have a wide range of health providers along with a 24/7 gymnasium for you to improve your health and wellbeing.</p>
  </div>

  <h2 class="expertise__title">OUR EXPERTISE</h2>
  <ul class="expertise__list">
    <li><svg width="24" height="16" viewBox="0 0 24 16"><circle cx="9" cy="8" r="7" fill="none" stroke="var(--tick)" stroke-width="2"/><path d="M5 8l4 4 12-11" fill="none" stroke="var(--tick)" stroke-width="2.5"/></svg>Exercise physiology</li>
    <li><svg width="24" height="16" viewBox="0 0 24 16"><circle cx="9" cy="8" r="7" fill="none" stroke="var(--tick)" stroke-width="2"/><path d="M5 8l4 4 12-11" fill="none" stroke="var(--tick)" stroke-width="2.5"/></svg>General fitness and well-being</li>
    <li><svg width="24" height="16" viewBox="0 0 24 16"><circle cx="9" cy="8" r="7" fill="none" stroke="var(--tick)" stroke-width="2"/><path d="M5 8l4 4 12-11" fill="none" stroke="var(--tick)" stroke-width="2.5"/></svg>Targeted programs (for example, strength<br>&amp; conditioning, workplace programs)</li>
    <li><svg width="24" height="16" viewBox="0 0 24 16"><circle cx="9" cy="8" r="7" fill="none" stroke="var(--tick)" stroke-width="2"/><path d="M5 8l4 4 12-11" fill="none" stroke="var(--tick)" stroke-width="2.5"/></svg>Nutrition and diet plans</li>
    <li><svg width="24" height="16" viewBox="0 0 24 16"><circle cx="9" cy="8" r="7" fill="none" stroke="var(--tick)" stroke-width="2"/><path d="M5 8l4 4 12-11" fill="none" stroke="var(--tick)" stroke-width="2.5"/></svg>Stress management</li>
    <li><svg width="24" height="16" viewBox="0 0 24 16"><circle cx="9" cy="8" r="7" fill="none" stroke="var(--tick)" stroke-width="2"/><path d="M5 8l4 4 12-11" fill="none" stroke="var(--tick)" stroke-width="2.5"/></svg>Injury recovery and prevention</li>
    <li><svg width="24" height="16" viewBox="0 0 24 16"><circle cx="9" cy="8" r="7" fill="none" stroke="var(--tick)" stroke-width="2"/><path d="M5 8l4 4 12-11" fill="none" stroke="var(--tick)" stroke-width="2.5"/></svg>Ergonomics in the workplace</li>
    <li><svg width="24" height="16" viewBox="0 0 24 16"><circle cx="9" cy="8" r="7" fill="none" stroke="var(--tick)" stroke-width="2"/><path d="M5 8l4 4 12-11" fill="none" stroke="var(--tick)" stroke-width="2.5"/></svg>Rehabilitation</li>
    <li><svg width="24" height="16" viewBox="0 0 24 16"><circle cx="9" cy="8" r="7" fill="none" stroke="var(--tick)" stroke-width="2"/><path d="M5 8l4 4 12-11" fill="none" stroke="var(--tick)" stroke-width="2.5"/></svg>Workcover and DVA</li>
  </ul>

  <div class="brand" style="left:713px;top:20px"><span class="brand__dot"></span><span class="brand__name">FITROVA</span></div>
  <div class="slogan" style="right:58px;top:82px;font-size:12px">We are here to improve your quality of life</div>
</section>

<section class="flyer flyer--back">
  <svg class="art" width="973" height="458" viewBox="0 0 973 458">
    <defs>
      <linearGradient id="gymBack" x1="0" y1="0" x2="1" y2="1">
        <stop offset="0" stop-color="#f2f2f2"/><stop offset=".5" stop-color="#e0e0e0"/><stop offset="1" stop-color="#cacaca"/>
      </linearGradient>
      <linearGradient id="svcDiet" x1="0" y1="0" x2="1" y2="1"><stop offset="0" stop-color="#9fd6f2"/><stop offset=".45" stop-color="#2f8fcf"/><stop offset=".75" stop-color="#6a6a6a"/><stop offset="1" stop-color="#d1352c"/></linearGradient>
      <linearGradient id="svcStrength" x1="0" y1="0" x2="1" y2="1"><stop offset="0" stop-color="#8a7a66"/><stop offset=".5" stop-color="#3a3a3a"/><stop offset=".8" stop-color="#c94a3c"/><stop offset="1" stop-color="#e6d5b8"/></linearGradient>
      <linearGradient id="svcKids" x1="0" y1="0" x2="1" y2="1"><stop offset="0" stop-color="#bfa78a"/><stop offset=".5" stop-color="#5a4a3e"/><stop offset="1" stop-color="#2c2c2c"/></linearGradient>
      <linearGradient id="svcChiro" x1="0" y1="0" x2="1" y2="1"><stop offset="0" stop-color="#fbfbfb"/><stop offset=".4" stop-color="#efe3c8"/><stop offset=".7" stop-color="#e2b896"/><stop offset="1" stop-color="#ffffff"/></linearGradient>
      <linearGradient id="svcPhys" x1="0" y1="0" x2="1" y2="1"><stop offset="0" stop-color="#f4ede6"/><stop offset=".5" stop-color="#dcc0a8"/><stop offset="1" stop-color="#2e6fa8"/></linearGradient>
      <linearGradient id="svcPhysio" x1="0" y1="0" x2="1" y2="1"><stop offset="0" stop-color="#bcd5ea"/><stop offset=".5" stop-color="#f0c9a9"/><stop offset="1" stop-color="#f7f7f7"/></linearGradient>
      <filter id="shadowB" x="-10%" y="-10%" width="120%" height="120%"><feDropShadow dx="2" dy="3" stdDeviation="3" flood-opacity=".45"/></filter>
    </defs>
    <rect width="973" height="458" fill="url(#gymBack)" role="img" aria-label="Faded photo of a gym interior"/>
    <polygon points="25,0 95,0 180,75 110,75" fill="var(--orange)"/>
    <polygon points="905,0 973,0 973,175 840,175" fill="var(--green)"/>
    <polygon points="0,180 92,180 0,285" fill="var(--green)"/>
    <polygon points="630,255 720,255 810,385 720,385" fill="var(--orange)"/>
    <polygon points="800,330 890,330 930,385 835,385" fill="var(--blue)"/>
    <g filter="url(#shadowB)">
      <polygon points="75,145 111,83 183,83 219,145 183,207 111,207" fill="url(#svcDiet)" stroke="#2a2a2a" stroke-width="6" role="img" aria-label="Photo of water bottles, dumbbells and a tape measure"/>
      <polygon points="200,247 236,185 308,185 344,247 308,309 236,309" fill="url(#svcStrength)" stroke="#2a2a2a" stroke-width="6" role="img" aria-label="Photo of people training on a fitness ball"/>
      <polygon points="330,147 366,85 438,85 474,147 438,209 366,209" fill="url(#svcKids)" stroke="#2a2a2a" stroke-width="6" role="img" aria-label="Photo of a coach training a young boy with a barbell"/>
      <polygon points="465,247 501,185 573,185 609,247 573,309 501,309" fill="url(#svcChiro)" stroke="#2a2a2a" stroke-width="6" role="img" aria-label="Photo of a chiropractor beside a spine model"/>
      <polygon points="598,152 634,90 706,90 742,152 706,214 634,214" fill="url(#svcPhys)" stroke="#2a2a2a" stroke-width="6" role="img" aria-label="Photo of a clinician assessing a patient"/>
      <polygon points="740,242 776,180 848,180 884,242 848,304 776,304" fill="url(#svcPhysio)" stroke="#2a2a2a" stroke-width="6" role="img" aria-label="Photo of hands treating a knee"/>
    </g>
    <polygon points="18,344 210,344 218,360 210,376 10,376 14,386 20,376" fill="var(--blue)"/>
    <polygon points="527,385 973,385 973,458 567,458" fill="var(--dark)"/>
    <polygon points="532,362 660,362 660,390 598,390 590,400 582,390 532,390" fill="#ffffff" stroke="var(--orange)" stroke-width="3"/>
  </svg>

  <h2 class="services__title">OUR SERVICES INCLUDE</h2>

  <div class="brand" style="left:748px;top:12px"><span class="brand__dot"></span><span class="brand__name">FITROVA</span></div>
  <div class="slogan" style="right:58px;top:58px;font-size:10.5px">We are here to improve your quality of life</div>

  <span class="service-label" style="left:147px;top:216px">DIETICIAN</span>
  <span class="service-label" style="left:272px;top:306px">STRENGTH CONDITIONING</span>
  <span class="service-label" style="left:404px;top:218px">KIDS PROGRAMS</span>
  <span class="service-label" style="left:537px;top:311px">CHIROPRACTOR</span>
  <span class="service-label" style="left:672px;top:218px">EXERCISE PHYSIOLOGY</span>
  <span class="service-label" style="left:812px;top:305px">PHYSIOTHERAPY</span>

  <div class="offer__tag">SAVE OVER $159,85 FOR</div>
  <div class="offer__headline">FREE 7 DAY TRIAL</div>
  <p class="offer__terms">Membership, classes &amp; personal training introductory month 3 personal training sessions and month 24/7 membership and classes for $99.95<br>(saving of over $159.85)<br>conditions: valid for new members only</p>

  <div class="contact__tab">CONTACT US</div>
  <div class="contact__phone">+612 90001234</div>
  <div class="contact__address">27 Harbour View Road,<br>Eastwood Sydney NSW 2122</div>
  <div class="contact__web">www.fitrova.club | &nbsp;sam@fitrova.club | lee@fitrova.club</div>
</section>

</body>
</html>
```